Timber Ridge Land Services Business Cards

Need to create a business card with the company logo "Timber Ridge Land Services". The business will provide forestry mulching for land clearing and vegetation control, brush and small tree removal, wildlife habitat improvement and trail and property access creation.

```html
<!DOCTYPE html>
<html lang="en">
<head>
<meta charset="utf-8">
<title>Timber Ridge Land Services – Business Cards</title>
<link rel="stylesheet" href="https://fonts.googleapis.com/css2?family=Lato:wght@400;700;900&display=swap">
<style>
  :root {
    --forest: #045c45;
    --forest-deep: #034c39;
    --leaf: #6abf5c;
    --paper: #ffffff;
    --ink: #1b1b1b;
    --backdrop: #e9e7e2;
  }
  * { box-sizing: border-box; margin: 0; padding: 0; }
  html, body {
    width: 1200px; height: 931px; overflow: hidden;
    background: var(--backdrop);
    font-family: "Lato", Arial, sans-serif;
  }
  .sheet {
    width: 1200px; height: 931px;
    display: flex; flex-direction: column; align-items: center; justify-content: center;
    gap: 40px;
  }
  .card {
    width: 680px; height: 389px;
    border-radius: 26px;
    box-shadow: 0 6px 20px rgba(0,0,0,.12);
    position: relative;
  }
  /* Back */
  .card--back {
    background: var(--forest);
    color: var(--paper);
    display: flex; flex-direction: column; align-items: center; justify-content: center;
    text-align: center;
  }
  .wordmark { font-weight: 900; letter-spacing: .04em; text-transform: uppercase; line-height: 1; }
  .card--back .wordmark { font-size: 46px; color: var(--paper); }
  .wordmark-sub { display: block; }
  .services {
    margin-top: 46px;
    font-size: 20px; line-height: 1.35;
    max-width: 560px;
  }
  /* Front */
  .card--front { background: var(--paper); color: var(--ink); }
  .card--front .brand {
    position: absolute; top: 62px; left: 0; right: 0;
    text-align: center;
  }
  .card--front .wordmark { font-size: 44px; color: var(--forest); }
  .brand-mark {
    display: inline-block; width: 16px; height: 16px; border-radius: 50%;
    background: var(--forest); margin-right: 12px; vertical-align: middle;
    position: relative; top: -4px;
  }
  .details {
    position: absolute; top: 196px; left: 70px; right: 50px;
    display: flex; align-items: center;
  }
  .person { text-align: right; padding-right: 26px; width: 280px; }
  .person-name { font-size: 30px; font-weight: 700; color: var(--forest); text-transform: uppercase; letter-spacing: .02em; }
  .person-role { font-size: 18px; margin-top: 4px; }
  .divider { width: 2px; height: 92px; background: var(--forest); }
  .contact { list-style: none; padding-left: 22px; font-size: 17px; }
  .contact li { display: flex; align-items: center; gap: 12px; line-height: 30px; }
  .contact svg { width: 18px; height: 18px; fill: var(--forest); flex: none; }
  .address {
    position: absolute; bottom: 42px; left: 0; right: 0;
    text-align: center; font-size: 19px;
  }
</style>
</head>
<body>
<main class="sheet">
  <section class="card card--back" aria-label="Card back">
    <h2 class="wordmark">Timber Ridge<span class="wordmark-sub">Land Services</span></h2>
    <p class="services">Forestry mulching for land clearing and vegetation control • Brush and small tree removal • Wildlife habitat improvement and Trail and property access creation</p>
  </section>

  <section class="card card--front" aria-label="Card front">
    <div class="brand">
      <h1 class="wordmark"><span class="brand-mark"></span>Timber Ridge Land Services</h1>
    </div>
    <div class="details">
      <div class="person">
        <p class="person-name">Daniel Harper</p>
        <p class="person-role">Managing Director</p>
      </div>
      <div class="divider"></div>
      <ul class="contact">
        <li><svg viewBox="0 0 24 24" aria-hidden="true"><path d="M6.6 10.8a15 15 0 0 0 6.6 6.6l2.2-2.2a1 1 0 0 1 1-.25 11.4 11.4 0 0 0 3.6.57 1 1 0 0 1 1 1V20a1 1 0 0 1-1 1A17 17 0 0 1 3 4a1 1 0 0 1 1-1h3.5a1 1 0 0 1 1 1c0 1.25.2 2.45.57 3.57a1 1 0 0 1-.25 1z"/></svg>044-555 218 930</li>
        <li><svg viewBox="0 0 24 24" aria-hidden="true"><path d="M2 5h20v14H2z M2 5l10 8 10-8" fill="none" stroke="#045c45" stroke-width="2"/></svg>hello@timberridgeland.com</li>
        <li><svg viewBox="0 0 24 24" aria-hidden="true"><circle cx="12" cy="12" r="9" fill="none" stroke="#045c45" stroke-width="2"/><path d="M3 12h18M12 3c3 3 3 15 0 18M12 3c-3 3-3 15 0 18" fill="none" stroke="#045c45" stroke-width="1.6"/></svg>www.timberridgeland.com</li>
      </ul>
    </div>
    <p class="address">88 Cedar Hollow Road, Millbrook 45452</p>
  </section>
</main>
</body>
</html>
```